Finance web application design

We need a design for a new responsive finance web application. It should look uber professional and modern.

Inspiration and design we like:

website:
http://www.brennickhale.com/

The application presented here:
http://markets.pelvantgrid.com/en/products/tools-applications/trading-investment-tools/zarvo-trading-software.html

https://apps.quillstore.example/us/app/ferncastle-for-tablet/id582917463?mt=8

The application presented here (Slatepad version):
https://apps.quillstore.example/en/app/trevik-forex-trading/id649205318?mt=8&utm_source=trevikButton

Target Market(s)

Private Investors

Industry/Entity Type

Finance

Number of Pages Required

5+ page

Font styles to use
Other font styles liked:
• Nobile

Requirements
Must have
• Colors for "up" changes: green
• Colors for "down" changes: red
• Fonts in tables must be very easy to read -
• Deliver design for all pages attached.
Nice to have
• A dark (gray) background
• Graphs should be shaded and partly transparent - orange or blue
• White text as "normal" - orange text / blue text for headers
Should not have
• White background

```html
<!DOCTYPE html>
<html lang="en">
<head>
<meta charset="utf-8">
<title>Ledgerwise – Dashboard</title>
<link rel="stylesheet" href="https://fonts.googleapis.com/css2?family=Open+Sans:wght@400;600;700&display=swap">
<style>
  :root{
    --bg:#25282f;
    --bar:#1c1e23;
    --header:#24262c;
    --line:#31343b;
    --text:#eef0f2;
    --muted:#5f636b;
    --orange:#f39322;
    --blue:#1a9ad6;
    --blue-dim:#1a5478;
    --red:#c8101c;
    --red-dim:#5a1a20;
    --badge:#d8323c;
    --green:#1fae5b;
    --avg:#c9402f;
  }
  *{box-sizing:border-box;margin:0;padding:0}
  html,body{width:1200px;height:977px;overflow:hidden;background:var(--bg)}
  body{position:relative;font-family:"Open Sans",Arial,sans-serif;color:var(--text)}
  .abs{position:absolute}

  /* header */
  .topbar{left:0;top:0;width:1200px;height:90px;background:var(--header)}
  .brand{display:flex;align-items:center;gap:8px;font-size:36px;font-weight:700;color:var(--orange);letter-spacing:-.5px}
  .brand-mark{width:14px;height:14px;background:var(--orange)}
  .top-brand{left:32px;top:20px}
  .tool-icon{top:32px}
  .search{left:527px;top:32px;width:226px;height:26px;background:#fff;border-radius:2px;font-size:11px;color:#8a8d92;padding:5px 10px}
  .search svg{position:absolute;right:9px;top:5px}
  .badge{width:14px;height:14px;border-radius:50%;background:var(--badge);font-size:8px;font-weight:700;color:#fff;text-align:center;line-height:14px}
  .user{left:1003px;top:34px;font-size:16px}
  .avatar{left:1094px;top:25px;width:36px;height:36px;border-radius:50%;background:radial-gradient(circle at 50% 40%,#b38c6e,#5a4a3c);border:2px solid #e9e9e9}

  /* nav */
  .mainnav{left:0;top:90px;width:1200px;height:93px;background:var(--bar)}
  .nav-item{position:absolute;top:10px;width:76px;height:70px;text-align:center;font-size:13px}
  .nav-item svg{display:block;margin:9px auto 10px}
  .nav-item.is-active{background:#15171a;border:1px solid #0d0e10;border-radius:3px}

  /* stats */
  .row-line{left:0;width:1200px;height:1px;background:var(--line)}
  .stat{font-size:14.5px;white-space:nowrap}
  .meter{height:42px}
  .meter-blue{left:320px;top:234px;width:665px;
    background:repeating-linear-gradient(90deg,var(--blue) 0 6px,transparent 6px 9px) 0 0/261px 100% no-repeat,
               repeating-linear-gradient(90deg,var(--blue-dim) 0 6px,transparent 6px 9px)}
  .meter-red{left:320px;top:464px;width:665px;height:44px;
    background:repeating-linear-gradient(90deg,var(--red) 0 6px,transparent 6px 9px) 0 0/495px 100% no-repeat,
               repeating-linear-gradient(90deg,var(--red-dim) 0 6px,transparent 6px 9px)}
  .meter-label{height:19px;padding:0 9px;background:var(--blue);border-radius:2px;font-size:10.5px;font-weight:600;line-height:19px;color:#fff}

  .chart-title{left:325px;top:528px;font-size:36px;font-weight:600;color:#dcdde0}
  .chart{left:327px;top:592px}
  .axis{top:880px;font-size:11px;font-weight:700;color:var(--muted);transform:translateX(-50%)}
  .avg-tag{left:1083px;top:750px;width:73px;height:27px;background:var(--avg);font-size:11px;font-weight:700;text-align:center;line-height:27px;border-radius:2px}

  /* footer */
  .footer{left:0;top:932px;width:1200px;height:45px;background:var(--bar)}
  .foot-brand{left:32px;top:3px;font-size:30px;color:#fff}
  .foot-brand .brand-mark{background:#fff;width:11px;height:11px}
  .foot-link{top:15px;font-size:13px}
  .dot{top:22px;width:4px;height:4px;border-radius:50%;background:#fff}
  .copy{right:35px;top:15px;font-size:13px}
</style>
</head>
<body>

<header class="abs topbar">
  <div class="abs brand top-brand"><span class="brand-mark"></span>Ledgerwise</div>
  <svg class="abs tool-icon" style="left:330px" width="20" height="24" viewBox="0 0 20 24"><g fill="#fff"><rect y="4" width="20" height="3"/><rect y="10.5" width="20" height="3"/><rect y="17" width="20" height="3"/></g></svg>
  <svg class="abs tool-icon" style="left:368px" width="20" height="24" viewBox="0 0 20 24"><g fill="none" stroke="#fff" stroke-width="3"><path d="M4 14a7 7 0 0 1 11-7"/><path d="M16 10a7 7 0 0 1-11 7"/></g><path d="M13 3l5 4-6 2z M7 21l-5-4 6-2z" fill="#fff"/></svg>
  <svg class="abs tool-icon" style="left:409px" width="21" height="24" viewBox="0 0 21 24"><g fill="#fff"><rect y="2" width="9" height="9"/><rect x="12" y="2" width="9" height="9"/><rect y="14" width="9" height="9"/><rect x="12" y="14" width="9" height="9"/></g></svg>

  <div class="abs search">Search
    <svg width="16" height="16" viewBox="0 0 16 16"><circle cx="9.5" cy="6.5" r="4.5" fill="none" stroke="#b5b7ba" stroke-width="1.5"/><path d="M6 10l-4 4" stroke="#b5b7ba" stroke-width="2"/></svg>
  </div>

  <svg class="abs" style="left:945px;top:37px" width="24" height="17" viewBox="0 0 24 17"><rect width="24" height="17" rx="1" fill="#fff"/><path d="M1 1l11 9 11-9" fill="none" stroke="#24262c" stroke-width="1.6"/></svg>
  <div class="abs badge" style="left:941px;top:32px">7</div>
  <div class="abs badge" style="left:991px;top:32px">3</div>
  <div class="abs user">Marten K <svg width="10" height="7" viewBox="0 0 10 7" style="margin-left:4px"><path d="M1 1l4 4 4-4" fill="none" stroke="#fff" stroke-width="2"/></svg></div>
  <div class="abs avatar" role="img" aria-label="User profile photo"></div>
  <svg class="abs" style="left:1147px;top:34px" width="22" height="22" viewBox="0 0 22 22"><g fill="#fff"><circle cx="11" cy="11" r="7"/><rect x="9" y="0" width="4" height="22"/><rect x="0" y="9" width="22" height="4"/><rect x="9" y="0" width="4" height="22" transform="rotate(45 11 11)"/><rect x="9" y="0" width="4" height="22" transform="rotate(-45 11 11)"/></g><circle cx="11" cy="11" r="3" fill="#24262c"/></svg>
</header>

<nav class="abs mainnav">
  <div class="nav-item is-active" style="left:31px">
    <svg width="22" height="20" viewBox="0 0 22 20"><path d="M1 1v18h20" fill="none" stroke="#fff" stroke-width="2"/><path d="M4 15l5-6 4 3 6-8" fill="none" stroke="#fff" stroke-width="2"/><path d="M4 16h2v3H4zM8 13h2v6H8zM12 14h2v5h-2zM16 10h2v9h-2z" fill="#fff"/></svg>Home</div>
  <div class="nav-item" style="left:148px">
    <svg width="28" height="24" viewBox="0 0 28 24"><rect x="1" y="5" width="24" height="18" rx="2" fill="#fff"/><path d="M4 5l12-4 3 4" fill="#fff"/><rect x="17" y="11" width="10" height="6" rx="1" fill="#1c1e23" stroke="#fff" stroke-width="1.5"/></svg>Funds</div>
  <div class="nav-item" style="left:265px">
    <svg width="26" height="26" viewBox="0 0 26 26"><rect x="1" y="3" width="24" height="22" rx="2" fill="none" stroke="#fff" stroke-width="2"/><rect x="1" y="3" width="24" height="5" fill="#fff"/><g fill="#fff"><rect x="5" y="11" width="3" height="3"/><rect x="10" y="11" width="3" height="3"/><rect x="15" y="11" width="3" height="3"/><rect x="20" y="11" width="2" height="3"/><rect x="5" y="16" width="3" height="3"/><rect x="10" y="16" width="3" height="3"/><rect x="15" y="16" width="3" height="3"/><rect x="20" y="16" width="2" height="3"/></g><path d="M7 0v6M19 0v6" stroke="#fff" stroke-width="2"/></svg>Planning</div>
  <div class="nav-item" style="left:382px">
    <svg width="24" height="32" viewBox="0 0 24 32" style="margin-top:2px"><path d="M8 6h8v9l7 14H1l7-14z" fill="none" stroke="#fff" stroke-width="2"/><path d="M4 23h16l3 6H1z" fill="#fff"/><circle cx="13" cy="2" r="1.5" fill="#fff"/><circle cx="17" cy="4" r="1" fill="#fff"/></svg>Resources</div>
  <div class="nav-item" style="left:498px">
    <svg width="20" height="26" viewBox="0 0 20 26"><rect x="1" y="1" width="18" height="24" rx="2" fill="none" stroke="#fff" stroke-width="2"/><rect x="4" y="4" width="12" height="5" fill="#fff"/><g fill="#fff"><rect x="4" y="12" width="3" height="3"/><rect x="9" y="12" width="3" height="3"/><rect x="14" y="12" width="2" height="3"/><rect x="4" y="17" width="3" height="3"/><rect x="9" y="17" width="3" height="3"/><rect x="14" y="17" width="2" height="3"/></g></svg>Inventory</div>
  <div class="nav-item" style="left:616px">
    <svg width="32" height="28" viewBox="0 0 32 28"><rect x="8" y="1" width="22" height="18" fill="none" stroke="#fff" stroke-width="2" transform="rotate(8 19 10)"/><rect x="2" y="7" width="22" height="18" fill="#1c1e23" stroke="#fff" stroke-width="2"/><path d="M4 23l6-7 4 4 3-3 5 6z" fill="#fff"/><circle cx="18" cy="12" r="2" fill="#fff"/></svg>Media</div>
  <div class="nav-item" style="left:733px">
    <svg width="24" height="28" viewBox="0 0 24 28"><path d="M12 2a8 8 0 0 1 8 8v7l3 4H1l3-4v-7a8 8 0 0 1 8-8z" fill="#fff"/><circle cx="12" cy="24" r="3" fill="#fff"/></svg>Alerts</div>
  <div class="nav-item" style="left:846px">
    <svg width="26" height="26" viewBox="0 0 22 22"><g fill="#fff"><circle cx="11" cy="11" r="7"/><rect x="9" y="0" width="4" height="22"/><rect x="0" y="9" width="22" height="4"/><rect x="9" y="0" width="4" height="22" transform="rotate(45 11 11)"/><rect x="9" y="0" width="4" height="22" transform="rotate(-45 11 11)"/></g><circle cx="11" cy="11" r="3" fill="#1c1e23"/></svg>Settings</div>
</nav>

<main>
  <div class="abs stat" style="left:33px;top:194px">Bars In test</div>
  <div class="abs stat" style="left:194px;top:194px">25334</div>
  <div class="abs stat" style="left:320px;top:194px">Ticks Modefied</div>
  <div class="abs stat" style="left:551px;top:194px">2626173</div>
  <div class="abs stat" style="left:751px;top:194px">Modeling Quality</div>
  <div class="abs stat" style="left:1122px;top:194px">9.00 %</div>
  <div class="abs row-line" style="top:221px"></div>

  <div class="abs stat" style="left:33px;top:248px">Mismatech Charts</div>
  <div class="abs stat" style="left:209px;top:248px">0</div>
  <div class="abs meter meter-blue" role="progressbar" aria-valuenow="45" aria-valuemin="0" aria-valuemax="100"></div>
  <div class="abs meter-label" style="left:517px;top:246px">45 .00%</div>
  <div class="abs row-line" style="top:289px"></div>

  <div class="abs stat" style="left:33px;top:304px">Initial Deposit</div>
  <div class="abs stat" style="left:176px;top:304px">10000000.000</div>
  <div class="abs row-line" style="top:335px"></div>

  <div class="abs stat" style="left:31px;top:356px">Total Net Profit</div>
  <div class="abs stat" style="left:184px;top:356px">84321.0.9</div>
  <div class="abs stat" style="left:320px;top:356px">Ticks Modefied</div>
  <div class="abs stat" style="left:551px;top:356px">2626173</div>
  <div class="abs stat" style="left:751px;top:356px">Modeling Quality</div>
  <div class="abs row-line" style="top:396px"></div>

  <div class="abs stat" style="left:33px;top:411px">Initial Deposit</div>
  <div class="abs stat" style="left:176px;top:411px">10000000.000</div>
  <div class="abs row-line" style="top:451px"></div>

  <div class="abs stat" style="left:33px;top:478px">Mismatech Charts</div>
  <div class="abs stat" style="left:209px;top:478px">0</div>
  <div class="abs meter-red" role="progressbar" aria-valuenow="76" aria-valuemin="0" aria-valuemax="100"></div>
  <div class="abs meter-label" style="left:737px;top:476px">76 .00%</div>

  <div class="abs stat" style="left:33px;top:531px">Initial Deposit</div>
  <div class="abs stat" style="left:176px;top:531px">10000000.000</div>
  <div class="abs stat" style="left:31px;top:583px">Total Net Profit</div>
  <div class="abs stat" style="left:184px;top:583px">84321.0.9</div>
  <div class="abs stat" style="left:33px;top:650px">Ticks Modefied</div>
  <div class="abs stat" style="left:186px;top:650px">2626173</div>
  <div class="abs stat" style="left:31px;top:715px">Total Net Profit</div>
  <div class="abs stat" style="left:184px;top:715px">84321.0.9</div>
  <div class="abs stat" style="left:184px;top:777px">84321.0.9</div>
  <div class="abs stat" style="left:176px;top:853px">10000000.000</div>

  <h1 class="abs chart-title">Maximal Draw Down Graph</h1>

  <svg class="abs chart" width="738" height="275" viewBox="0 0 738 275">
    <defs>
      <pattern id="grid" width="23" height="23" patternUnits="userSpaceOnUse">
        <path d="M23 0V23H0" fill="none" stroke="#353840" stroke-width="1"/>
      </pattern>
      <clipPath id="above"><rect width="738" height="171"/></clipPath>
      <clipPath id="below"><rect y="171" width="738" height="104"/></clipPath>
    </defs>
    <rect width="738" height="275" fill="#272a31"/>
    <rect width="738" height="275" fill="url(#grid)"/>
    <rect y="171" width="738" height="104" fill="#5a4a3a" opacity=".85"/>
    <path id="area" d="M0 205L20 194L46 189L69 188L107 180L133 177L179 177L211 169L263 156L309 156L352 153L404 151L442 132L466 137L481 129L529 125L555 114L582 117L620 104L648 99L668 100L709 89L738 92V171H0Z" fill="#1f6a48" opacity=".75" clip-path="url(#above)"/>
    <path d="M0 205L20 194L46 189L69 188L107 180L133 177L179 177L211 169L263 156L309 156L352 153L404 151L442 132L466 137L481 129L529 125L555 114L582 117L620 104L648 99L668 100L709 89L738 92V171H0Z" fill="#8a2a26" opacity=".85" clip-path="url(#below)"/>
    <line x1="0" y1="171" x2="738" y2="171" stroke="var(--avg)" stroke-width="1.5"/>
    <polyline points="0,205 20,194 46,189 69,188 107,180 133,177 179,177 211,169 263,156 309,156 352,153 404,151 442,132 466,137 481,129 529,125 555,114 582,117 620,104 648,99 668,100 709,89 738,92" fill="none" stroke="var(--green)" stroke-width="3" stroke-linejoin="round"/>
    <g fill="#0f3a23" stroke="var(--green)" stroke-width="2.5">
      <circle cx="20" cy="194" r="4.5"/><circle cx="46" cy="189" r="4.5"/><circle cx="69" cy="188" r="4.5"/>
      <circle cx="107" cy="180" r="4.5"/><circle cx="133" cy="177" r="4.5"/><circle cx="179" cy="177" r="4.5"/>
      <circle cx="211" cy="169" r="4.5"/><circle cx="263" cy="156" r="4.5"/><circle cx="309" cy="156" r="4.5"/>
      <circle cx="352" cy="153" r="4.5"/><circle cx="404" cy="151" r="4.5"/><circle cx="442" cy="132" r="4.5"/>
      <circle cx="466" cy="137" r="4.5"/><circle cx="529" cy="125" r="4.5"/><circle cx="555" cy="114" r="4.5"/>
      <circle cx="582" cy="117" r="4.5"/><circle cx="620" cy="104" r="4.5"/><circle cx="648" cy="99" r="4.5"/>
      <circle cx="668" cy="100" r="4.5"/><circle cx="709" cy="89" r="4.5"/>
    </g>
    <circle cx="481" cy="129" r="5" fill="#fff" stroke="var(--green)" stroke-width="2.5"/>
    <rect x="448" y="73" width="66" height="40" rx="2" fill="#3b3e45"/>
    <path d="M476 113l5 6 5-6z" fill="#3b3e45"/>
    <text x="481" y="88" text-anchor="middle" font-family="Open Sans, sans-serif" font-size="9" font-weight="600" fill="#b9bbbf">25th</text>
    <text x="481" y="103" text-anchor="middle" font-family="Open Sans, sans-serif" font-size="13" font-weight="700" fill="#fff">$42,325</text>
  </svg>

  <div class="abs avg-tag">AVERAGE</div>

  <span class="abs axis" style="left:356px">October 09</span>
  <span class="abs axis" style="left:444px">January 10</span>
  <span class="abs axis" style="left:520px">April 10</span>
  <span class="abs axis" style="left:584px">July 10</span>
  <span class="abs axis" style="left:658px">October 10</span>
  <span class="abs axis" style="left:743px">January 11</span>
  <span class="abs axis" style="left:815px">April 11</span>
  <span class="abs axis" style="left:879px">July 11</span>
  <span class="abs axis" style="left:953px">October 11</span>
  <span class="abs axis" style="left:1037px">January 12</span>
</main>

<footer class="abs footer">
  <div class="abs brand foot-brand"><span class="brand-mark"></span>Ledgerwise</div>
  <span class="abs foot-link" style="left:266px">Home</span>
  <span class="abs dot" style="left:326px"></span>
  <span class="abs foot-link" style="left:359px">Funds</span>
  <span class="abs dot" style="left:425px"></span>
  <span class="abs foot-link" style="left:454px">Planning</span>
  <span class="abs dot" style="left:524px"></span>
  <span class="abs foot-link" style="left:551px">Resources</span>
  <span class="abs dot" style="left:641px"></span>
  <span class="abs foot-link" style="left:664px">Inventory</span>
  <span class="abs dot" style="left:742px"></span>
  <span class="abs foot-link" style="left:765px">Media</span>
  <span class="abs dot" style="left:818px"></span>
  <span class="abs foot-link" style="left:847px">Alerts</span>
  <span class="abs dot" style="left:903px"></span>
  <span class="abs foot-link" style="left:928px">Settings</span>
  <span class="abs copy">2014 © Ledgerwise.</span>
</footer>

</body>
</html>
```